Four in One (Flexible infographic for Content Management Industry)

See attachment.
A graphic depicting 4 products, where each can stand on its own and each can be combined with others, but where, if all are taken together, the best result is achieved (the "super product").
Intended use is web. See attached file as an example.
The most basic idea is as the attached diagram shows, where 4 rectangles are arranged in a quadrangle, with a middle rectangle in the center representing the combined 4 products. This concept is fine except it is a bit too obvious as it stands. We are looking for either a variation of this or another concept.
The audience is technical + professional + enterprise - NOT consumers. Hence the design should be conservative in nature.
We are aware of tools like as Canva or Pictogram where such graphics are available, but we are looking for something with a bit more imagination and flexibility.
This graphic should be targeted to web sites and be delivered with vector-based (SVG) graphics.

```html
<!DOCTYPE html>
<html lang="en">
<head>
<meta charset="utf-8">
<title>Four in One – Super Product</title>
<link href="https://fonts.googleapis.com/css2?family=Figtree:wght@400;500;700;800&display=swap" rel="stylesheet">
<style>
  :root {
    --bg: #e8e8e9;
    --sheet: #ffffff;
    --purple: #8b18e6;
    --navy: #172a63;
    --blue: #2e74e6;
    --teal: #22ddd2;
    --ink: #1f2430;
    --hub-ink: #17365d;
    --gear: #1a4a6b;
    --pill: #f0f0f2;
    --pill-ink: #1f2f5c;
  }
  html, body {
    margin: 0;
    width: 1200px;
    height: 1200px;
    overflow: hidden;
    background: var(--bg);
  }
  .infographic { display: block; width: 1200px; height: 1200px; font-family: "Figtree", sans-serif; }
  .sheet { fill: var(--sheet); }
  .frame { fill: none; stroke-width: 3; stroke-linecap: butt; }
  .frame--purple { stroke: var(--purple); }
  .frame--navy { stroke: var(--navy); }
  .frame--blue { stroke: var(--blue); }
  .frame--teal { stroke: var(--teal); }
  .header { font-size: 29px; font-weight: 700; }
  .header--purple { fill: var(--purple); }
  .header--navy { fill: var(--navy); }
  .header--blue { fill: var(--blue); }
  .header--teal { fill: var(--teal); }
  .body-copy { font-size: 21px; font-weight: 400; fill: var(--ink); }
  .bullet { font-size: 19px; font-weight: 400; fill: var(--ink); letter-spacing: 0.6px; }
  .tick { fill: none; stroke-width: 1.8; stroke-linecap: round; stroke-linejoin: round; }
  .tick--purple { stroke: var(--purple); }
  .tick--navy { stroke: var(--navy); }
  .tick--blue { stroke: var(--blue); }
  .tick--teal { stroke: var(--teal); }
  .pill { fill: var(--pill); }
  .pill-label { font-size: 19px; font-weight: 700; fill: var(--pill-ink); letter-spacing: 4px; }
  .badge-ring { fill: var(--sheet); }
  .badge--purple { fill: var(--purple); }
  .badge--navy { fill: var(--navy); }
  .badge--blue { fill: var(--blue); }
  .badge--teal { fill: var(--teal); }
  .glyph { fill: #ffffff; }
  .hub { fill: var(--sheet); }
  .hub-title { font-size: 38px; font-weight: 800; fill: var(--hub-ink); }
  .gear { fill: var(--gear); }
</style>
</head>
<body>
<svg class="infographic" viewBox="0 0 1932 1932" xmlns="http://www.w3.org/2000/svg" role="img" aria-label="Four products combining into one super product">
  <defs>
    <filter id="soft-shadow" x="-20%" y="-20%" width="140%" height="140%">
      <feDropShadow dx="0" dy="2" stdDeviation="4" flood-color="#000" flood-opacity="0.16"/>
    </filter>
    <symbol id="tick" viewBox="-12 -12 24 24" overflow="visible">
      <circle r="10.5"/>
      <path d="M-4.5 0.5 L-1.2 3.8 L4.8 -3.2"/>
    </symbol>
  </defs>

  <rect class="sheet" x="178" y="375" width="1576" height="1181"/>

  <!-- Frames flowing into the central rings -->
  <path class="frame frame--purple" d="M943 632 V441 Q943 421 923 421 H328 Q308 421 308 441 V922 Q308 942 328 942 H723 A245 245 0 0 1 1209 942"/>
  <path class="frame frame--navy" d="M1299 942 H1606 Q1626 942 1626 922 V441 Q1626 421 1606 421 H1010 Q990 421 990 441 V688 A279 279 0 0 1 990 1244"/>
  <path class="frame frame--blue" d="M634 989 H328 Q308 989 308 1009 V1489 Q308 1509 328 1509 H923 Q943 1509 943 1489 V1244 A279 279 0 0 1 943 688"/>
  <path class="frame frame--teal" d="M990 1299 V1489 Q990 1509 1010 1509 H1606 Q1626 1509 1626 1489 V1009 Q1626 989 1606 989 H1210 A245 245 0 0 1 722 989"/>

  <!-- Hub -->
  <g class="hub-group">
    <circle class="hub" cx="966" cy="966" r="182" filter="url(#soft-shadow)"/>
    <g class="gear" transform="translate(966 910)">
      <circle r="44"/>
      <g>
        <rect x="-9" y="-55" width="18" height="16" rx="2"/>
        <rect x="-9" y="-55" width="18" height="16" rx="2" transform="rotate(45)"/>
        <rect x="-9" y="-55" width="18" height="16" rx="2" transform="rotate(90)"/>
        <rect x="-9" y="-55" width="18" height="16" rx="2" transform="rotate(-45)"/>
        <rect x="-9" y="-55" width="18" height="16" rx="2" transform="rotate(-90)"/>
        <rect x="-9" y="-55" width="18" height="16" rx="2" transform="rotate(135)"/>
        <rect x="-9" y="-55" width="18" height="16" rx="2" transform="rotate(-135)"/>
      </g>
      <path fill="#ffffff" d="M0 -30 C-20 -30 -31 -15 -31 0 C-31 12 -24 19 -18 26 V40 H18 V26 C24 19 31 12 31 0 C31 -15 20 -30 0 -30 Z"/>
      <path fill="none" stroke="#1a4a6b" stroke-width="4" stroke-linecap="round" d="M-7 30 V8 M7 30 V8 M-7 8 a5 5 0 1 1 7 -4 a5 5 0 1 1 7 4"/>
      <rect x="-14" y="44" width="28" height="6" rx="2"/>
      <rect x="-9" y="53" width="18" height="5" rx="2"/>
    </g>
    <text class="hub-title" x="966" y="1028" text-anchor="middle">SUPER</text>
    <text class="hub-title" x="966" y="1066" text-anchor="middle">PRODUCT</text>
  </g>

  <!-- Panel: top left -->
  <g class="panel panel--left">
    <text class="header header--purple" x="406" y="503">Header Text Here</text>
    <text class="body-copy" x="406" y="539">Lorem ipsum dolor sit amet,</text>
    <text class="body-copy" x="406" y="567">consectetur adipiscing elit, sed</text>
    <text class="body-copy" x="406" y="595">do eiusmod tempor incididunt ut</text>
    <text class="body-copy" x="406" y="623">labore et dolore magna aliqua.</text>
    <use href="#tick" class="tick tick--purple" x="418" y="665" width="24" height="24" transform="translate(-12 -12)"/>
    <use href="#tick" class="tick tick--purple" x="418" y="706" width="24" height="24" transform="translate(-12 -12)"/>
    <use href="#tick" class="tick tick--purple" x="418" y="747" width="24" height="24" transform="translate(-12 -12)"/>
    <use href="#tick" class="tick tick--purple" x="418" y="790" width="24" height="24" transform="translate(-12 -12)"/>
    <text class="bullet" x="446" y="672">Insert bullet text here</text>
    <text class="bullet" x="446" y="713">Insert bullet text here</text>
    <text class="bullet" x="446" y="754">Insert bullet text here</text>
    <text class="bullet" x="446" y="797">Insert bullet text here</text>
    <rect class="pill" x="406" y="843" width="252" height="45" rx="22.5"/>
    <text class="pill-label" x="532" y="873" text-anchor="middle">LEARN MORE</text>
  </g>

  <!-- Panel: top right -->
  <g class="panel panel--right">
    <text class="header header--navy" x="1524" y="503" text-anchor="end">Header Text Here</text>
    <text class="body-copy" x="1524" y="539" text-anchor="end">Lorem ipsum dolor sit amet,</text>
    <text class="body-copy" x="1524" y="567" text-anchor="end">consectetur adipiscing elit, sed</text>
    <text class="body-copy" x="1524" y="595" text-anchor="end">do eiusmod tempor incididunt ut</text>
    <text class="body-copy" x="1524" y="623" text-anchor="end">labore et dolore magna aliqua.</text>
    <use href="#tick" class="tick tick--navy" x="1512" y="665" width="24" height="24" transform="translate(-12 -12)"/>
    <use href="#tick" class="tick tick--navy" x="1512" y="706" width="24" height="24" transform="translate(-12 -12)"/>
    <use href="#tick" class="tick tick--navy" x="1512" y="747" width="24" height="24" transform="translate(-12 -12)"/>
    <use href="#tick" class="tick tick--navy" x="1512" y="790" width="24" height="24" transform="translate(-12 -12)"/>
    <text class="bullet" x="1486" y="672" text-anchor="end">Insert bullet text here</text>
    <text class="bullet" x="1486" y="713" text-anchor="end">Insert bullet text here</text>
    <text class="bullet" x="1486" y="754" text-anchor="end">Insert bullet text here</text>
    <text class="bullet" x="1486" y="797" text-anchor="end">Insert bullet text here</text>
    <rect class="pill" x="1273" y="843" width="251" height="45" rx="22.5"/>
    <text class="pill-label" x="1399" y="873" text-anchor="middle">LEARN MORE</text>
  </g>

  <!-- Panel: bottom left -->
  <g class="panel panel--left" transform="translate(0 568)">
    <text class="header header--blue" x="406" y="503">Header Text Here</text>
    <text class="body-copy" x="406" y="539">Lorem ipsum dolor sit amet,</text>
    <text class="body-copy" x="406" y="567">consectetur adipiscing elit, sed</text>
    <text class="body-copy" x="406" y="595">do eiusmod tempor incididunt ut</text>
    <text class="body-copy" x="406" y="623">labore et dolore magna aliqua.</text>
    <use href="#tick" class="tick tick--blue" x="418" y="665" width="24" height="24" transform="translate(-12 -12)"/>
    <use href="#tick" class="tick tick--blue" x="418" y="706" width="24" height="24" transform="translate(-12 -12)"/>
    <use href="#tick" class="tick tick--blue" x="418" y="747" width="24" height="24" transform="translate(-12 -12)"/>
    <use href="#tick" class="tick tick--blue" x="418" y="790" width="24" height="24" transform="translate(-12 -12)"/>
    <text class="bullet" x="446" y="672">Insert bullet text here</text>
    <text class="bullet" x="446" y="713">Insert bullet text here</text>
    <text class="bullet" x="446" y="754">Insert bullet text here</text>
    <text class="bullet" x="446" y="797">Insert bullet text here</text>
    <rect class="pill" x="406" y="843" width="252" height="45" rx="22.5"/>
    <text class="pill-label" x="532" y="873" text-anchor="middle">LEARN MORE</text>
  </g>

  <!-- Panel: bottom right -->
  <g class="panel panel--right" transform="translate(0 568)">
    <text class="header header--teal" x="1524" y="503" text-anchor="end">Header Text Here</text>
    <text class="body-copy" x="1524" y="539" text-anchor="end">Lorem ipsum dolor sit amet,</text>
    <text class="body-copy" x="1524" y="567" text-anchor="end">consectetur adipiscing elit, sed</text>
    <text class="body-copy" x="1524" y="595" text-anchor="end">do eiusmod tempor incididunt ut</text>
    <text class="body-copy" x="1524" y="623" text-anchor="end">labore et dolore magna aliqua.</text>
    <use href="#tick" class="tick tick--teal" x="1512" y="665" width="24" height="24" transform="translate(-12 -12)"/>
    <use href="#tick" class="tick tick--teal" x="1512" y="706" width="24" height="24" transform="translate(-12 -12)"/>
    <use href="#tick" class="tick tick--teal" x="1512" y="747" width="24" height="24" transform="translate(-12 -12)"/>
    <use href="#tick" class="tick tick--teal" x="1512" y="790" width="24" height="24" transform="translate(-12 -12)"/>
    <text class="bullet" x="1486" y="672" text-anchor="end">Insert bullet text here</text>
    <text class="bullet" x="1486" y="713" text-anchor="end">Insert bullet text here</text>
    <text class="bullet" x="1486" y="754" text-anchor="end">Insert bullet text here</text>
    <text class="bullet" x="1486" y="797" text-anchor="end">Insert bullet text here</text>
    <rect class="pill" x="1273" y="843" width="251" height="45" rx="22.5"/>
    <text class="pill-label" x="1399" y="873" text-anchor="middle">LEARN MORE</text>
  </g>

  <!-- Badges -->
  <g class="badge" transform="translate(308 682)">
    <circle class="badge-ring" r="84" filter="url(#soft-shadow)"/>
    <circle class="badge--purple" r="67"/>
    <path class="glyph" d="M-20 -34 H20 Q26 -34 26 -28 V10 L8 30 H-20 Q-26 30 -26 24 V-28 Q-26 -34 -20 -34 Z"/>
    <g fill="var(--purple)">
      <rect x="-16" y="-22" width="28" height="5" rx="2.5"/>
      <rect x="-16" y="-11" width="32" height="5" rx="2.5"/>
      <rect x="-16" y="0" width="18" height="5" rx="2.5"/>
      <path d="M6 28 V14 Q6 10 10 10 H24 Z"/>
    </g>
  </g>

  <g class="badge" transform="translate(1625 682)">
    <circle class="badge-ring" r="84" filter="url(#soft-shadow)"/>
    <circle class="badge--navy" r="67"/>
    <path class="glyph" d="M-22 12 a14 14 0 0 1 -2 -28 a20 20 0 0 1 38 -6 a16 16 0 0 1 14 18 Z"/>
    <circle r="19" cx="16" cy="12" fill="#ffffff" stroke="var(--navy)" stroke-width="5"/>
    <path d="M8 12 L14 18 L24 7" fill="none" stroke="var(--navy)" stroke-width="4" stroke-linecap="round" stroke-linejoin="round"/>
  </g>

  <g class="badge" transform="translate(308 1249)">
    <circle class="badge-ring" r="84" filter="url(#soft-shadow)"/>
    <circle class="badge--blue" r="67"/>
    <rect class="glyph" x="-30" y="-30" width="26" height="26" rx="6"/>
    <rect class="glyph" x="4" y="-30" width="26" height="26" rx="6" transform="rotate(45 17 -17)"/>
    <rect class="glyph" x="-30" y="4" width="26" height="26" rx="6"/>
    <rect class="glyph" x="4" y="4" width="26" height="26" rx="6"/>
  </g>

  <g class="badge" transform="translate(1625 1249)">
    <circle class="badge-ring" r="84" filter="url(#soft-shadow)"/>
    <circle class="badge--teal" r="67"/>
    <g fill="none" stroke="#ffffff" stroke-width="5" stroke-linejoin="round" stroke-linecap="round">
      <path d="M0 -32 L32 -12 L0 8 L-32 -12 Z"/>
      <path d="M-32 0 L0 20 L32 0"/>
      <path d="M-32 12 L0 32 L32 12"/>
      <path d="M-10 -10 L0 -17 L10 -10"/>
    </g>
  </g>
</svg>
</body>
</html>
```